Criação de Papelaria para Brisa & Aurora
" Clinica Multidiciplinar com equipamentos de alta tecnologia para tratamentos esteticos faciais e corporais "

```html
<!DOCTYPE html>
<html lang="pt-BR">
<head>
<meta charset="utf-8">
<title>Brisa &amp; Aurora — Cartão de visita</title>
<link rel="stylesheet" href="https://fonts.googleapis.com/css2?family=Montserrat:wght@200;300;400;700&display=swap">
<style>
  :root {
    --backdrop: #8a8a8a;
    --card-dark: #4b4b4b;
    --card-light: #f4f4f4;
    --ink-dark: #2e2e2e;
    --ink-soft: #5a5a5a;
    --ink-on-dark: #e9e9e9;
  }
  * { margin: 0; padding: 0; box-sizing: border-box; }
  html, body { width: 1200px; height: 1200px; overflow: hidden; }
  body {
    background: var(--backdrop);
    font-family: "Montserrat", sans-serif;
    position: relative;
  }
  .card {
    position: absolute;
    left: 200px;
    width: 800px;
    height: 457px;
    box-shadow: 0 10px 30px rgba(0,0,0,0.25);
  }
  .card--front { top: 120px; background: var(--card-dark); display: flex; align-items: center; justify-content: center; }
  .card--back { top: 623px; background: var(--card-light); color: var(--ink-dark); }
  .brand-name {
    font-weight: 200;
    text-transform: uppercase;
    letter-spacing: 0.32em;
    font-size: 40px;
  }
  .card--front .brand-name { color: var(--ink-on-dark); }
  .card--back .brand-name {
    position: absolute; top: 52px; right: 56px;
    font-size: 30px; color: var(--ink-dark);
  }
  .holder {
    position: absolute; left: 60px; top: 170px;
  }
  .holder-first { font-weight: 300; font-size: 26px; }
  .holder-last { font-weight: 700; font-size: 26px; letter-spacing: 0.06em; text-transform: uppercase; }
  .holder-role { font-weight: 300; font-size: 17px; color: var(--ink-soft); margin-top: 4px; }
  .contacts {
    position: absolute; left: 60px; bottom: 48px;
    font-size: 15px; font-weight: 400; line-height: 1.7; color: var(--ink-soft);
  }
  .contacts .web { margin-top: 10px; font-size: 17px; color: var(--ink-dark); }
  .address {
    position: absolute; right: 56px; bottom: 48px;
    text-align: right; font-size: 15px; line-height: 1.7; color: var(--ink-soft);
  }
</style>
</head>
<body>
  <section class="card card--front">
    <p class="brand-name">Brisa &amp; Aurora</p>
  </section>

  <section class="card card--back">
    <p class="brand-name">Brisa &amp; Aurora</p>
    <div class="holder">
      <p class="holder-first">Helena Costa</p>
      <p class="holder-last">Ribeiro</p>
      <p class="holder-role">Esteticista</p>
    </div>
    <div class="contacts">
      <p>21 2000-4510</p>
      <p>21 98000-1234</p>
      <p>contato@brisaeaurora.com.br</p>
      <p class="web">www.brisaeaurora.com.br</p>
    </div>
    <div class="address">
      <p>Rua das Acácias 240</p>
      <p>Loja 12 - Centro</p>
      <p>Rio de Janeiro - 20000-100</p>
    </div>
  </section>
</body>
</html>
```